Weight Loss Banner Ad

We need banner ads for our website, www.brightplatekitchen.com. We would like to see Banner ads that represent what you think is the most captivating aspect of The MealWise Plan. Please review the website.

The banner ad should be something you REALLY want to click on. It needs to include the name and/or logo and the slogan "Gourmet Meals Direct To Your House"

We will want the final ad in multiple sizes but it should use the same image and copy.

Logo is attached, so are images. Feel free to use your own if you think you have a better on

Size (pixels):
468 x 60
392 x 72
234 x 60
125 x 125
120 x 90
120 x 60
88 x 31
120 x 240
120 x 600
160 x 600

Target Market(s)

Fitness Enthusiast looking to lose weight.

Industry/Entity Type

Weight

Font styles to use
Sans Serif

Requirements
Must have
• See Description
Nice to have
• Should be awesome and make you want to buy some food. Also you may want to say something about the price:

i.e. Starting at only $99

```html
<!DOCTYPE html>
<html lang="en">
<head>
<meta charset="utf-8">
<title>The MealWise Plan – Banner Ads</title>
<link rel="stylesheet" href="https://fonts.googleapis.com/css2?family=Open+Sans:wght@400;600;700;800&family=Tinos&display=swap">
<style>
  :root {
    --green: #8cc63f;
    --grey-band: #8d8d8d;
    --grey-text: #676767;
    --ink: #1f1f1f;
    --panel: #f5f5f5;
    --frame: #c9c9c9;
    --gold-top: #ffe46b;
    --gold-bottom: #f2a600;
    --gold-edge: #c98a00;
    --button-rim-top: #eeeeee;
    --button-rim-bottom: #9a9a9a;
    --photo-greens: #7aa04a;
    --photo-warm: #c98a5a;
    --photo-skin: #d9b49a;
    --photo-dark: #4a3a33;
    --white: #ffffff;
  }
  * { box-sizing: border-box; margin: 0; padding: 0; }
  html, body { width: 923px; height: 1200px; overflow: hidden; background: var(--white); }
  body { position: relative; font-family: "Open Sans", Arial, sans-serif; color: var(--grey-text); }

  .banner {
    position: absolute;
    background: var(--panel);
    border: 1px solid var(--frame);
    overflow: hidden;
  }
  .banner--skyscraper { left: 26px; top: 52px; width: 299px; height: 1111px; }
  .banner--rectangle  { left: 345px; top: 375px; width: 557px; height: 461px; }

  .header-shape { position: absolute; display: block; }
  .brand-name {
    position: absolute;
    font-family: "Open Sans", Arial, sans-serif;
    font-weight: 700;
    color: var(--white);
    text-align: right;
    line-height: 1.08;
    letter-spacing: -0.3px;
    white-space: nowrap;
  }

  .headline-accent { font-weight: 800; color: var(--green); letter-spacing: -0.5px; white-space: nowrap; }
  .headline-main { font-weight: 800; color: var(--grey-text); letter-spacing: -0.5px; white-space: nowrap; }
  .slogan { font-weight: 400; color: var(--grey-text); line-height: 1.2; text-align: center; }
  .price-lead { font-weight: 600; color: var(--ink); white-space: nowrap; }

  .price-badge {
    position: absolute;
    border-radius: 50%;
    background: var(--green);
    color: var(--ink);
    display: flex; align-items: center; justify-content: center;
    font-weight: 600;
  }
  .price-badge sup { font-size: 0.55em; position: relative; top: -0.45em; margin-right: 1px; vertical-align: baseline; }

  .order-button {
    position: absolute;
    padding: 7px;
    border-radius: 4px;
    background: linear-gradient(var(--button-rim-top), var(--button-rim-bottom));
  }
  .order-button span {
    display: flex; align-items: center; justify-content: center;
    width: 100%; height: 100%;
    background: linear-gradient(var(--gold-top), var(--gold-bottom));
    border: 1px solid var(--gold-edge);
    color: var(--ink);
    font-family: "Tinos", Georgia, serif;
  }

  .photo { position: absolute; }

  /* Skyscraper */
  .banner--skyscraper .brand-name { right: 18px; top: 36px; font-size: 34px; }
  .banner--skyscraper .headline-accent { position: absolute; top: 268px; width: 100%; text-align: center; font-size: 41px; }
  .banner--skyscraper .headline-main { position: absolute; top: 318px; width: 100%; text-align: center; font-size: 56px; }
  .banner--skyscraper .slogan { position: absolute; top: 402px; width: 100%; font-size: 30px; }
  .banner--skyscraper .photo {
    left: 0; top: 557px; width: 100%; height: 330px;
    background: linear-gradient(120deg, var(--photo-greens) 0%, #a7c46a 28%, var(--photo-warm) 55%, #b06a7a 78%, #e8e2d8 100%);
  }
  .banner--skyscraper .price-lead { position: absolute; left: 18px; top: 912px; font-size: 26px; }
  .banner--skyscraper .price-badge { left: 219px; top: 895px; width: 76px; height: 76px; font-size: 40px; }
  .banner--skyscraper .order-button { left: 15px; top: 970px; width: 265px; height: 72px; }
  .banner--skyscraper .order-button span { font-size: 33px; }
  .site-strip {
    position: absolute; left: 0; bottom: 0; width: 100%; height: 63px;
    background: var(--green);
    display: flex; align-items: center; justify-content: center;
    color: var(--ink); font-weight: 600; font-size: 23px;
  }

  /* Rectangle */
  .banner--rectangle .photo {
    left: 0; top: 0; width: 300px; height: 100%;
    background: radial-gradient(ellipse at 55% 85%, #e9eef0 0%, #d2dcd0 22%, transparent 45%),
                linear-gradient(180deg, var(--photo-dark) 0%, var(--photo-skin) 38%, #e6d2c2 70%, #f1ece6 100%);
  }
  .banner--rectangle .brand-name { right: 20px; top: 12px; font-size: 28px; }
  .banner--rectangle .headline-block { position: absolute; right: 22px; top: 150px; text-align: right; }
  .banner--rectangle .headline-accent { font-size: 32px; line-height: 1.1; }
  .banner--rectangle .headline-main { font-size: 45px; line-height: 1.05; }
  .banner--rectangle .slogan { position: absolute; left: 215px; top: 236px; width: 330px; font-size: 24px; }
  .banner--rectangle .price-lead { position: absolute; left: 292px; top: 317px; font-size: 23px; }
  .banner--rectangle .price-badge { left: 478px; top: 282px; width: 76px; height: 76px; font-size: 37px; }
  .banner--rectangle .order-button { left: 296px; top: 362px; width: 236px; height: 64px; }
  .banner--rectangle .order-button span { font-size: 29px; }
  .banner--rectangle .site-address { position: absolute; left: 285px; top: 428px; width: 258px; text-align: center; font-size: 22px; color: var(--ink); }
</style>
</head>
<body>

<section class="banner banner--skyscraper" aria-label="Skyscraper banner">
  <svg class="header-shape" width="299" height="175" viewBox="0 0 299 175" style="left:0;top:0">
    <path d="M0 0 H299 V118 Q150 172 0 150 Z" fill="var(--grey-band)"/>
    <path d="M0 150 Q150 172 299 118 V132 Q150 186 0 164 Z" fill="var(--green)"/>
  </svg>
  <div class="brand-name">The MealWise<br>Plan</div>

  <div class="headline-accent">WORRY FREE</div>
  <div class="headline-main">FITNESS!</div>
  <p class="slogan">Gourmet Meals<br>Direct To<br>Your House</p>

  <div class="photo" role="img" aria-label="Photo of grilled vegetables and lettuce on a white platter"></div>

  <div class="price-lead">Starting at only</div>
  <div class="price-badge"><sup>$</sup>99</div>

  <a class="order-button"><span>Order Now</span></a>

  <div class="site-strip">brightplatekitchen.com</div>
</section>

<section class="banner banner--rectangle" aria-label="Rectangle banner">
  <div class="photo" role="img" aria-label="Photo of a woman eating a fresh salad from a white bowl"></div>

  <svg class="header-shape" width="380" height="120" viewBox="0 0 380 120" style="left:177px;top:0">
    <path d="M0 0 H380 V82 H230 Q120 82 60 40 Q30 18 0 0 Z" fill="var(--grey-band)"/>
    <path d="M0 0 Q30 18 60 40 Q120 82 230 82 H380 V92 H226 L210 118 L198 92 Q110 90 55 50 Q25 25 0 0 Z" fill="var(--green)"/>
  </svg>
  <div class="brand-name">The MealWise<br>Plan</div>

  <div class="headline-block">
    <div class="headline-accent">WORRY FREE</div>
    <div class="headline-main">FITNESS!</div>
  </div>
  <p class="slogan">Gourmet Meals Direct To<br>Your House</p>

  <div class="price-lead">Starting at only</div>
  <div class="price-badge"><sup>$</sup>99</div>

  <a class="order-button"><span>Order Now</span></a>
  <div class="site-address">brightplatekitchen.com</div>
</section>

</body>
</html>
```